Board to put on a meditation centre - Lantern Hill Haven

I need a board design for a new meditation centre based in Oslo which offers free courses in meditation and self-empowerment. The size of the board is width 374cm x height 104cm.  The name of the meditation centre together with subtitles should be on the board but also some elegant decoration that matches the theme (lantern hill haven/meditation).
Here is the website of the meditation centre to give you a feeling of it: https://lyktebakkenkurs.no/
Good if you can use a blue color close to this one: rgb(37, 180, 193) as well as some brown/golden color (similar to the palette on the website).
On the board it should say:
Lyktebakken senter (in big letters, the rest is subtitles)
Meditasjon & Spirituell visdom
Kurs - Retreat - Dialog
lyktebakkenkurs.no
The design should be very elegant and beautiful and the feeling should be of "An Lantern Hill Haven". A logo is here attached and should be used but I need to get a better quality version of it, will upload that as soon as possible.

```html
<!DOCTYPE html>
<html lang="no">
<head>
<meta charset="utf-8">
<title>Lyktebakken senter – skilt</title>
<link rel="stylesheet" href="https://fonts.googleapis.com/css2?family=Montserrat:wght@800&family=Roboto:wght@400;500;700&display=swap">
<style>
  :root {
    --red: #f0082c;
    --ink: #262626;
    --grey: #3a3a3a;
    --beige: #c8bba8;
    --mandala: #eeeeee;
    --white: #ffffff;
    --page: #ffffff;
  }
  html, body {
    margin: 0;
    width: 1200px;
    height: 1200px;
    overflow: hidden;
    background: var(--page);
  }
  .board {
    position: absolute;
    left: 30px;
    top: 442px;
    width: 1140px;
    height: 316px;
    background: var(--white);
    box-shadow: 0 10px 28px rgba(0,0,0,0.22);
    overflow: hidden;
  }
  .board-art {
    position: absolute;
    inset: 0;
  }
  .title {
    position: absolute;
    left: 38px;
    top: 22px;
    margin: 0;
    font-family: "Montserrat", sans-serif;
    font-weight: 800;
    font-size: 66px;
    line-height: 1;
    letter-spacing: -1px;
    color: var(--ink);
    white-space: nowrap;
  }
  .title .accent { color: var(--red); }
  .subtitle {
    position: absolute;
    left: 38px;
    top: 104px;
    margin: 0;
    font-family: "Roboto", sans-serif;
    font-weight: 400;
    font-size: 33px;
    color: var(--ink);
    white-space: nowrap;
  }
  .offers {
    position: absolute;
    left: 40px;
    top: 180px;
    display: flex;
    align-items: center;
    gap: 26px;
    margin: 0;
    padding: 0;
    list-style: none;
  }
  .offer {
    display: flex;
    align-items: center;
    gap: 10px;
    font-family: "Roboto", sans-serif;
    font-weight: 500;
    font-size: 19px;
    color: var(--ink);
  }
  .offer-icon {
    width: 48px;
    height: 48px;
    border-radius: 6px;
    background: var(--red);
    display: block;
  }
  .partner {
    position: absolute;
    left: 530px;
    top: 192px;
    display: flex;
    align-items: center;
    gap: 10px;
    font-family: "Roboto", sans-serif;
    font-weight: 400;
    font-size: 17px;
    letter-spacing: 2px;
    color: var(--grey);
    white-space: nowrap;
  }
  .partner-dot {
    width: 26px;
    height: 26px;
    border-radius: 50%;
    background: var(--red);
  }
  .web {
    position: absolute;
    left: 40px;
    top: 250px;
    height: 54px;
    line-height: 54px;
    margin: 0;
    font-family: "Roboto", sans-serif;
    font-weight: 700;
    font-size: 31px;
    letter-spacing: 3px;
    color: var(--white);
  }
</style>
</head>
<body>
  <main class="board">
    <svg class="board-art" viewBox="0 0 1140 316" width="1140" height="316" aria-hidden="false">
      <defs>
        <linearGradient id="photo-tones" x1="0" y1="0" x2="1" y2="1">
          <stop offset="0" stop-color="#7d8a5a"/>
          <stop offset="0.45" stop-color="#9aa07c"/>
          <stop offset="0.75" stop-color="#c9c4bb"/>
          <stop offset="1" stop-color="#8fa6b8"/>
        </linearGradient>
      </defs>
      <!-- red info band -->
      <polygon class="web-band" points="0,250 815,250 761,304 0,304" fill="var(--red)"/>
      <!-- ornament area -->
      <circle class="mandala" cx="916" cy="92" r="98" fill="var(--mandala)" role="img" aria-label="Light grey circular mandala ornament"/>
      <!-- beige accent stripe -->
      <polygon class="accent-stripe" points="1080,0 1094,0 778,316 764,316" fill="var(--beige)"/>
      <!-- photo panel -->
      <polygon class="photo" points="1106,0 1140,0 1140,316 790,316" fill="url(#photo-tones)" role="img" aria-label="Photo of a woman meditating cross-legged on a wooden boardwalk beside tall grass"/>
      <!-- corner accent -->
      <polygon class="corner-white" points="1140,205 1140,220 1036,316 1021,316" fill="var(--white)"/>
      <polygon class="corner-red" points="1140,220 1140,316 1036,316" fill="var(--red)"/>
    </svg>

    <h1 class="title">LYKTEBAKKEN <span class="accent">SENTER</span></h1>
    <p class="subtitle">MEDITASJON &amp; SPIRITUELL VISDOM</p>

    <ul class="offers">
      <li class="offer">
        <svg class="offer-icon" viewBox="0 0 48 48" role="img" aria-label="Kurs">
          <rect width="48" height="48" rx="6" fill="var(--red)"/>
          <circle cx="24" cy="14" r="4" fill="#fff"/>
          <path d="M24 19 L30 32 H18 Z" fill="#fff"/>
          <rect x="13" y="32" width="22" height="4" rx="2" fill="#fff"/>
        </svg>
        KURS
      </li>
      <li class="offer">
        <svg class="offer-icon" viewBox="0 0 48 48" role="img" aria-label="Retreat">
          <rect width="48" height="48" rx="6" fill="var(--red)"/>
          <path d="M24 12 C29 18 29 26 24 33 C19 26 19 18 24 12 Z" fill="none" stroke="#fff" stroke-width="2"/>
          <path d="M12 20 C19 21 23 27 24 33 C17 32 13 27 12 20 Z" fill="none" stroke="#fff" stroke-width="2"/>
          <path d="M36 20 C29 21 25 27 24 33 C31 32 35 27 36 20 Z" fill="none" stroke="#fff" stroke-width="2"/>
        </svg>
        RETREAT
      </li>
      <li class="offer">
        <svg class="offer-icon" viewBox="0 0 48 48" role="img" aria-label="Dialog">
          <rect width="48" height="48" rx="6" fill="var(--red)"/>
          <rect x="14" y="18" width="20" height="20" rx="6" fill="#fff"/>
          <rect x="15" y="10" width="4.5" height="14" rx="2.2" fill="#fff"/>
          <rect x="20.5" y="8" width="4.5" height="16" rx="2.2" fill="#fff"/>
          <rect x="26" y="10" width="4.5" height="14" rx="2.2" fill="#fff"/>
        </svg>
        DIALOG
      </li>
    </ul>

    <div class="partner">
      <span class="partner-dot"></span>
      STILLVANN AKADEMI
    </div>

    <p class="web">WWW.LYKTEBAKKENKURS.NO</p>
  </main>
</body>
</html>
```